Compass & Canvas needs new business card design

I need a new business card design. I'm looking for out-of-the-box design which represents the freedom of being a location independent entrepreneur.
I offer coaching, retreats and trips.
I would like to see designs with and without the photo.
Colors I use are black (#000000), green (#25A796) and brown (#D7C38C)
Website compassandcanvas.net

Target Market(s)

location independent entrepreneurs, digital nomads, people looking to swap the 9 to 5 for a lifestyle business

Industry/Entity Type

Business

Contact Information for Business Card

Daria Tolsen
Your Lifestyle Business Coach, Retreat & Trip Leader
http://compassandcanvas.net
hello@compassandcanvas.net
Live a life you don't need a holiday from

Font styles to use
Serif
Sans Serif

Requirements
Must have
• One side should contain only the logo. I would also consider having the "Live a life you don't need a holiday from" on that side too (depending on how it looks)
• Please show both sides on the designs.

```html
<!DOCTYPE html>
<html lang="en">
<head>
<meta charset="utf-8">
<title>Compass &amp; Canvas — Business Card</title>
<link rel="stylesheet" href="https://fonts.googleapis.com/css2?family=Bebas+Neue&family=Source+Sans+3:wght@400;600&display=swap">
<style>
  :root {
    --ink: #1d1d1d;
    --green: #25A796;
    --sand: #D7C38C;
    --paper: #ffffff;
    --backdrop: #2a2a2a;
  }
  * { margin: 0; padding: 0; box-sizing: border-box; }
  html, body { width: 1200px; height: 987px; overflow: hidden; }
  body {
    background: var(--backdrop);
    font-family: "Source Sans 3", "Helvetica Neue", Arial, sans-serif;
    position: relative;
  }
  .card {
    position: absolute;
    left: 293px;
    width: 615px;
    height: 352px;
    overflow: hidden;
  }
  .card--front { top: 130px; background: var(--paper); }
  .card--back { top: 505px; background: var(--sand); }

  .wordmark {
    font-family: "Bebas Neue", "Arial Narrow", sans-serif;
    font-weight: 400;
    color: var(--ink);
    letter-spacing: 1px;
    line-height: 1;
  }
  .card--front .wordmark {
    position: absolute;
    left: 42px;
    top: 44px;
    font-size: 50px;
  }

  .person { position: absolute; left: 40px; top: 150px; }
  .person__name {
    color: var(--green);
    font-weight: 600;
    font-size: 22px;
    line-height: 1.2;
    margin-bottom: 4px;
  }
  .person__role {
    color: var(--ink);
    font-size: 17px;
    line-height: 1.35;
  }

  .wave { position: absolute; inset: 0; width: 615px; height: 352px; }

  .contact {
    position: absolute;
    right: 30px;
    top: 255px;
    color: var(--paper);
    text-align: right;
    font-size: 15.5px;
    line-height: 23px;
  }
  .contact__row { display: flex; justify-content: flex-end; align-items: center; gap: 10px; }
  .contact__icon { width: 14px; height: 14px; flex: none; }
  .tagline {
    position: absolute;
    right: 30px;
    top: 308px;
    font-family: "Bebas Neue", "Arial Narrow", sans-serif;
    font-size: 19px;
    letter-spacing: 0.4px;
    color: var(--paper);
  }

  .backdrop-pattern { position: absolute; inset: 0; background: var(--sand); }
  .card--back .wordmark {
    position: absolute;
    left: 0; right: 0;
    top: 148px;
    text-align: center;
    font-size: 62px;
  }
</style>
</head>
<body>

  <section class="card card--front" aria-label="Business card front">
    <svg class="wave" viewBox="0 0 615 352" aria-hidden="true">
      <path d="M0,272 C130,305 300,292 420,212 C515,148 580,70 615,2 L615,352 L0,352 Z" fill="var(--green)"/>
      <path d="M0,268 C130,300 300,287 418,207 C512,144 576,66 610,0" fill="none" stroke="var(--ink)" stroke-width="7" stroke-linecap="round"/>
    </svg>

    <div class="wordmark">Compass &amp; Canvas</div>

    <div class="person">
      <p class="person__name">Daria Tolsen</p>
      <p class="person__role">Your Lifestyle Business Coach<br>Retreat &amp; Trip Leader</p>
    </div>

    <div class="contact">
      <div class="contact__row">
        <span>compassandcanvas.net</span>
        <svg class="contact__icon" viewBox="0 0 14 14" aria-hidden="true">
          <circle cx="7" cy="7" r="6.5" fill="var(--paper)"/>
          <path d="M3,5 Q5,3 7,4 T9,7 T6,10 M9,2.5 Q11,4 10,6" fill="none" stroke="var(--green)" stroke-width="1.4"/>
        </svg>
      </div>
      <div class="contact__row">
        <span>hello@compassandcanvas.net</span>
        <svg class="contact__icon" viewBox="0 0 14 14" aria-hidden="true">
          <rect x="0.5" y="3" width="13" height="9" fill="var(--paper)"/>
          <path d="M0.5,3 L7,8 L13.5,3" fill="none" stroke="var(--green)" stroke-width="1.2"/>
        </svg>
      </div>
    </div>
    <p class="tagline">Live a life you don't need a holiday from</p>
  </section>

  <section class="card card--back" aria-label="Business card back">
    <div class="backdrop-pattern" role="img" aria-label="Faint repeated brand name pattern on sand background"></div>
    <div class="wordmark">Compass &amp; Canvas</div>
  </section>

</body>
</html>
```